Marlow's Pantry Home Page Design

Hello CraftHive -

I am looking for a home page design for an Indian Food Grocery ecommerce site with a store in Boulder, CO. This design request is just for the home page (http://marlowspantry.example/), including new design, font, layout and emblem/word mark logo.

What: Marlow's Pantry (spices, lentils, rice, frozen foods, etc.)

Desired Color Scheme: Warm, earth tones (red, orange, yellow), that remind the guest of Indian Spices

Tone: This is an Indian-American family owned, small business catering imported Indian foods and spices to a primary market of Indian-Americans and a secondary market of Indian food/spice lovers.

Themes to communicate: Indian, family owned, food

Sample Websites: http://www.vantelkitchen.example/, http://www.brambleshop.example/, http://www.quelvaro.example/

Please feel free to reach out with any questions. Thank you.

Target Market(s)

Indian-Americans (1st and 2nd Generation)

Industry/Entity Type

Small Business

Requirements
Must have
• Final Design must be delivered in layered PSD file with all fonts and licenses used.

```html
<!DOCTYPE html>
<html lang="en">
<head>
<meta charset="utf-8">
<title>Marlow's Pantry</title>
<link rel="stylesheet" href="https://fonts.googleapis.com/css2?family=Signika:wght@400;600&family=Crimson+Text&family=Arimo:wght@400&display=swap">
<style>
:root{
  --red:#c80c0c;
  --red-dark:#a80808;
  --footer-red:#f40404;
  --orange:#f59a0a;
  --orange-light:#fdb220;
  --gold:#f6c200;
  --gold-dark:#d79f00;
  --text-orange:#e0720a;
  --price:#d00d0d;
  --grey:#6a6a6a;
  --line:#d8d8d8;
  --white:#fff;
}
*{margin:0;padding:0;box-sizing:border-box}
html,body{width:1158px;height:1200px;overflow:hidden;background:var(--white);font-family:"Arimo",Arial,sans-serif}
.page{position:relative;width:1158px;height:1200px;background:linear-gradient(#e4e4e4 148px,#fff 250px)}
.abs{position:absolute}
.header{left:0;top:0;width:1158px;height:100px;background:var(--red)}
.brand{left:174px;top:22px;color:var(--white);font-family:"Signika",sans-serif;font-weight:600;font-size:28px;letter-spacing:1.5px}
.slogan{left:173px;top:54px;color:#fbe4e4;font-family:"Crimson Text",serif;font-size:14px}
.cart-tag{left:696px;top:31px;width:87px;height:32px;background:var(--orange-light);clip-path:polygon(0 0,100% 0,94% 100%,0 100%);color:var(--white);font-family:"Signika",sans-serif;font-size:11px;line-height:32px;padding-left:25px}
.cart-badge{left:645px;top:15px;width:64px;height:64px;border-radius:50%;background:var(--orange);border:4px solid var(--white);box-shadow:0 0 0 2px #f3c07a}
.search{left:822px;top:35px;width:165px;height:30px;background:var(--white)}
.nav{left:0;top:100px;width:1158px;height:48px;background:linear-gradient(var(--orange-light),var(--orange));display:flex;justify-content:center}
.nav ul{list-style:none;display:flex;margin-left:-3px}
.nav li{color:var(--white);font-family:"Signika",sans-serif;font-size:11.5px;line-height:48px;padding:0 13px;border-left:1px solid rgba(255,255,255,.25)}
.nav li:first-child{border-left:0}
.slider{left:171px;top:166px;width:816px;height:318px;border-radius:12px;background:#b9b9b9;padding:3px}
.slide{width:100%;height:100%;border-radius:10px;background:linear-gradient(120deg,#e0431c 0%,#b85a3a 30%,#e9a995 55%,#a2552e 75%,#4f6e2a 100%)}
.thumbs{left:382px;top:491px;height:50px;display:flex;align-items:center}
.arrow-l,.arrow-r{width:26px;height:50px;display:flex;align-items:center;justify-content:center}
.arrow-l{background:var(--red);border-radius:25px 0 0 25px}
.arrow-r{background:var(--orange);border-radius:0 25px 25px 0}
.thumb{width:68px;height:50px;border-right:1px solid #fff}
.t1{background:linear-gradient(#b8442c,#5f8a2d)}.t2{background:linear-gradient(#e9d3b6,#c5794a)}.t3{background:linear-gradient(#e46d1f,#6d2a10)}.t4{background:linear-gradient(#d8e49a,#a0b62e)}.t5{background:linear-gradient(#5a3a24,#c89a3c)}
.products{left:171px;top:571px;width:816px;height:413px;border:1px solid #cfcfcf;border-radius:16px;background:var(--white)}
.products h2{position:absolute;left:19px;top:19px;color:#e60d0d;font-family:"Signika",sans-serif;font-weight:600;font-size:14px}
.products .rule{position:absolute;left:11px;right:11px;top:47px;border-top:1px solid var(--line)}
.pager{position:absolute;left:758px;top:20px;display:flex;gap:6px}
.card{position:absolute;top:61px;width:172px}
.card .img{width:172px;height:172px;background:radial-gradient(circle at 55% 45%,#c2622a 0 22%,#3f6d2a 23% 32%,#f2f0ec 50%,#dcdad6 100%)}
.card h3{margin:10px 0 0 8px;font-weight:400;font-size:10px;color:var(--text-orange)}
.card p{margin:10px 0 0 8px;font-size:9.6px;line-height:14.5px;color:var(--grey);letter-spacing:.2px}
.card .price{margin:8px 0 0 7px;font-size:17px;color:var(--price)}
.card .meta{display:flex;justify-content:space-between;align-items:center;margin:6px 0 0 8px;font-size:9.6px;color:var(--grey)}
.card .meta svg{display:block}
.card .btn{margin:13px 0 0 8px;width:71px;height:25px;background:linear-gradient(var(--gold),#f0b400);border:1px solid var(--gold-dark);border-radius:2px;font-size:10px;line-height:23px;text-align:center;color:#333}
.footer{left:171px;top:999px;width:816px;height:166px;background:var(--footer-red);border-radius:16px}
.footer ul{position:absolute;top:13px;list-style:none}
.footer li{color:var(--white);font-size:10px;line-height:20.4px}
.footer .label{position:absolute;left:618px;color:var(--white);font-size:9.4px}
.footer .field{position:absolute;left:618px;width:157px;height:19px;background:var(--white);border:1px solid #ddd;font-size:8.5px;color:#888;line-height:17px;padding-left:7px}
.flags{position:absolute;left:716px;top:19px;display:flex;gap:8px}
.flags span{width:15px;height:10px;display:block}
.social{position:absolute;left:618px;top:116px;display:flex;gap:10px}
.social span{width:21px;height:21px;border-radius:50%;background:var(--white);display:block;opacity:.95}
.copy{left:196px;top:1176px;font-size:9.6px;color:#777}
.mark{left:940px;top:1176px;font-size:9.6px;color:#888}
</style>
</head>
<body>
<div class="page">
  <header class="abs header"></header>
  <div class="abs brand">MARLOW'S PANTRY</div>
  <div class="abs slogan">slogan comes here</div>
  <div class="abs cart-tag">0 ITEMS</div>
  <div class="abs cart-badge">
    <svg width="56" height="56" viewBox="0 0 56 56"><rect x="17" y="24" width="22" height="14" rx="2" fill="#fff"/><rect x="15" y="21" width="26" height="4" fill="#fff"/><path d="M28 21 L33 13" stroke="#fff" stroke-width="2"/><g stroke="#f59a0a" stroke-width="1.5"><path d="M22 28v7M26 28v7M30 28v7M34 28v7"/></g></svg>
  </div>
  <div class="abs search">
    <svg width="24" height="30" viewBox="0 0 24 30"><circle cx="12" cy="13" r="5" fill="none" stroke="#999" stroke-width="2"/><path d="M16 17l4 5" stroke="#999" stroke-width="2.5"/></svg>
  </div>
  <nav class="abs nav"><ul>
    <li>APPETIZERS</li><li>DESSERTS</li><li>FRUITS &amp; VEGETABLES</li><li>MEAT</li><li>PIZZA-PASTA</li><li>SEAFOOD</li><li>SIDE DISHES</li><li>SNACKS</li><li>CONTACT US</li>
  </ul></nav>

  <div class="abs slider"><div class="slide" role="img" aria-label="Close-up of a deli sandwich with ham, onion, tomato and parsley"></div></div>
  <div class="abs thumbs">
    <div class="arrow-l"><svg width="10" height="16"><path d="M8 1L2 8l6 7" stroke="#fff" stroke-width="2" fill="none"/></svg></div>
    <div class="thumb t1" role="img" aria-label="Sliced deli meats"></div>
    <div class="thumb t2" role="img" aria-label="Rice dish on a plate"></div>
    <div class="thumb t3" role="img" aria-label="Roasted pastries"></div>
    <div class="thumb t4" role="img" aria-label="Lime drink"></div>
    <div class="thumb t5" role="img" aria-label="Fries and vegetables"></div>
    <div class="arrow-r"><svg width="10" height="16"><path d="M2 1l6 7-6 7" stroke="#fff" stroke-width="2" fill="none"/></svg></div>
  </div>

  <section class="abs products">
    <h2>NEW PRODUCTS</h2>
    <div class="rule"></div>
    <div class="pager">
      <svg width="12" height="12"><circle cx="6" cy="6" r="6" fill="#d9a000"/><path d="M7 3L4 6l3 3" fill="#fff"/></svg>
      <svg width="12" height="12"><circle cx="6" cy="6" r="6" fill="#d9a000"/><path d="M5 3l3 3-3 3" fill="#fff"/></svg>
    </div>
    <div class="card" style="left:21px">
      <div class="img" role="img" aria-label="Grilled salmon fillet with asparagus and lemon"></div>
      <h3>EIUSMOD TEMPOR</h3><p>Set ipsum dolor sit amet conse<br>ctetur adipisicing elit</p>
      <div class="price">$273.89</div>
      <div class="meta"><svg width="60" height="10"><g fill="#f2bf00"><circle cx="5" cy="5" r="4"/><circle cx="17" cy="5" r="4"/></g><g fill="#ddd"><circle cx="29" cy="5" r="4"/><circle cx="41" cy="5" r="4"/><circle cx="53" cy="5" r="4"/></g></svg><span>2 Review(s)</span></div>
      <div class="btn">Add to cart</div>
    </div>
    <div class="card" style="left:223px">
      <div class="img" role="img" aria-label="Grilled salmon fillet with asparagus and lemon"></div>
      <h3>EIUSMOD TEMPOR</h3><p>Set ipsum dolor sit amet conse<br>ctetur adipisicing elit</p>
      <div class="price">$273.89</div>
      <div class="meta"><svg width="60" height="10"><g fill="#f2bf00"><circle cx="5" cy="5" r="4"/><circle cx="17" cy="5" r="4"/></g><g fill="#ddd"><circle cx="29" cy="5" r="4"/><circle cx="41" cy="5" r="4"/><circle cx="53" cy="5" r="4"/></g></svg><span>2 Review(s)</span></div>
      <div class="btn">Add to cart</div>
    </div>
    <div class="card" style="left:426px">
      <div class="img" role="img" aria-label="Grilled salmon fillet with asparagus and lemon"></div>
      <h3>EIUSMOD TEMPOR</h3><p>Set ipsum dolor sit amet conse<br>ctetur adipisicing elit</p>
      <div class="price">$273.89</div>
      <div class="meta"><svg width="60" height="10"><g fill="#f2bf00"><circle cx="5" cy="5" r="4"/><circle cx="17" cy="5" r="4"/></g><g fill="#ddd"><circle cx="29" cy="5" r="4"/><circle cx="41" cy="5" r="4"/><circle cx="53" cy="5" r="4"/></g></svg><span>2 Review(s)</span></div>
      <div class="btn">Add to cart</div>
    </div>
    <div class="card" style="left:628px">
      <div class="img" role="img" aria-label="Grilled salmon fillet with asparagus and lemon"></div>
      <h3>EIUSMOD TEMPOR</h3><p>Set ipsum dolor sit amet conse<br>ctetur adipisicing elit</p>
      <div class="price">$273.89</div>
      <div class="meta"><svg width="60" height="10"><g fill="#f2bf00"><circle cx="5" cy="5" r="4"/><circle cx="17" cy="5" r="4"/></g><g fill="#ddd"><circle cx="29" cy="5" r="4"/><circle cx="41" cy="5" r="4"/><circle cx="53" cy="5" r="4"/></g></svg><span>2 Review(s)</span></div>
      <div class="btn">Add to cart</div>
    </div>
  </section>

  <footer class="abs footer">
    <ul style="left:41px"><li>About</li><li>Customer Service</li><li>Site Map</li><li>Search Terms</li><li>Advanced Search</li><li>Orders and Returns</li><li>Contacts</li></ul>
    <ul style="left:228px"><li>Shipping &amp; Returns</li><li>Secure Shopping</li><li>International Shipping</li><li>Affiliates</li><li>Group Sales</li><li>Secure Shopping</li><li>Secure Shopping</li></ul>
    <ul style="left:432px"><li>Sign In</li><li>View Cart</li><li>My Wishlist</li><li>Track My Order</li><li>Help</li><li>Sign In</li><li>View Cart</li></ul>
    <div class="label" style="top:19px">CURRENCIES</div>
    <div class="flags">
      <span style="background:linear-gradient(#000 33%,#d00 33% 66%,#fc0 66%)"></span>
      <span style="background:linear-gradient(#c60b1e 25%,#ffc400 25% 75%,#c60b1e 75%)"></span>
      <span style="background:#1c3f94"></span>
    </div>
    <div class="field" style="top:37px">US Dollar</div>
    <div class="label" style="top:63px">EMAIL SIGNUP</div>
    <div class="field" style="top:80px">Please, enter your e-mail</div>
    <div class="social"><span></span><span></span><span></span><span></span></div>
  </footer>
  <div class="abs copy">Copyright © 2012 Marlow's Pantry. All Rights Reserved.</div>
  <div class="abs mark">M3</div>
</div>
</body>
</html>
```